Brightmere Holdings - Business Cards

We would need to design our Company Business Cards for the following People:

1. Thomas Pirelli
Director/Licensee-In-Charge
M: 0412 579 304
T: (02) 7314 2296
E: thomas@brightmere.com.au
Website: www.brightmereholdings.com

2. Marcus Holt
Project Manager
M: 0421 367 915
T: (02) 7314 2296
E: marcus@brightmereholdings.com

3. Priya Ravindrasekar
Property Officer
M: 0477 218 643
T: (02) 7314 2296
E: priya@brightmereholdings.com

Address: Level 9, 27 Harbour Lane W, Parramatta NSW 2150
The above address is the SAME for ALL Cards.

This Card is to be Double-Sided.
Front - With the above Information & Details.
Back - Showing the Services:
Property Services, Financial Solutions, Special Projects.

ALL Office Locations:
Sydney: (02) 7314 2296
Melbourne: (03) 9241 5503
Brisbane: (07) 3466 1982
Malaysia (JB): (+601) 7293 6048
Singapore: (+65) 9182 4637

We intend on making a Design/Template for the Business Card & duplicating these Business Cards for the above 3x People.
Please USE & REFER to the above FULL Name, Job Title, Mobile, Office Phone, Email & Website.

```html
<!DOCTYPE html>
<html lang="en">
<head>
<meta charset="utf-8">
<title>Brightmere Holdings – Business Cards</title>
<link rel="stylesheet" href="https://fonts.googleapis.com/css2?family=Roboto:wght@400;500;700&display=swap">
<style>
  :root {
    --page-bg: #e9e9ea;
    --card-dark: #0d0d0d;
    --card-light: #ffffff;
    --accent: #b7c41c;
    --ink: #141414;
    --ink-soft: #2a2a2a;
    --on-dark: #ffffff;
    --on-dark-soft: #b9b9b9;
  }
  * { box-sizing: border-box; margin: 0; padding: 0; }
  html, body {
    width: 1200px;
    height: 1000px;
    overflow: hidden;
    background: var(--page-bg);
    font-family: "Roboto", Arial, sans-serif;
  }
  .sheet { position: relative; width: 1200px; height: 1000px; }
  .card {
    position: absolute;
    left: 250px;
    width: 700px;
    height: 400px;
    border-radius: 28px;
    overflow: hidden;
    box-shadow: 0 10px 28px rgba(0,0,0,0.18);
  }

  /* Back of card */
  .card--back { top: 70px; background: var(--card-dark); }
  .card--back .wordmark {
    position: absolute;
    left: 0; right: 0;
    top: 120px;
    text-align: center;
    color: var(--on-dark);
    font-weight: 400;
    font-size: 38px;
    letter-spacing: 9px;
    text-transform: uppercase;
  }
  .services {
    position: absolute;
    left: 0; right: 0;
    top: 196px;
    display: flex;
    justify-content: center;
    gap: 28px;
    list-style: none;
    color: var(--accent);
    font-weight: 500;
    font-size: 14px;
    letter-spacing: 2.5px;
    text-transform: uppercase;
  }
  .offices {
    position: absolute;
    left: 70px; right: 70px;
    bottom: 44px;
    display: grid;
    grid-template-columns: repeat(3, auto);
    justify-content: center;
    column-gap: 36px;
    row-gap: 8px;
    list-style: none;
    color: var(--on-dark-soft);
    font-size: 13px;
    line-height: 18px;
  }
  .offices b { color: var(--on-dark); font-weight: 500; margin-right: 6px; }

  /* Front of card */
  .card--front { top: 530px; background: var(--card-light); }
  .accent-tab {
    position: absolute;
    left: 0; top: 42px;
    width: 18px; height: 54px;
    background: var(--accent);
  }
  .person { position: absolute; left: 42px; top: 42px; }
  .person__name {
    color: var(--accent);
    font-weight: 700;
    font-size: 24px;
    line-height: 1.1;
  }
  .person__role {
    margin-top: 6px;
    color: var(--ink);
    font-weight: 400;
    font-size: 16px;
  }
  .card--front .wordmark {
    position: absolute;
    right: 44px;
    top: 150px;
    color: var(--ink);
    font-weight: 400;
    font-size: 30px;
    letter-spacing: 7px;
    text-transform: uppercase;
  }
  .contacts {
    position: absolute;
    left: 38px;
    bottom: 36px;
    list-style: none;
  }
  .contacts li {
    display: flex;
    align-items: center;
    gap: 12px;
    color: var(--ink-soft);
    font-size: 16px;
    line-height: 26px;
  }
  .contacts svg {
    width: 16px; height: 16px;
    flex: none;
    fill: none;
    stroke: var(--accent);
    stroke-width: 1.8;
    stroke-linecap: round;
    stroke-linejoin: round;
  }
</style>
</head>
<body>
<main class="sheet">

  <section class="card card--back" aria-label="Card back">
    <p class="wordmark">Brightmere Holdings</p>
    <ul class="services">
      <li>Property Services</li>
      <li>Financial Solutions</li>
      <li>Special Projects</li>
    </ul>
    <ul class="offices">
      <li><b>Sydney</b>(02) 7314 2296</li>
      <li><b>Melbourne</b>(03) 9241 5503</li>
      <li><b>Brisbane</b>(07) 3466 1982</li>
      <li><b>Malaysia (JB)</b>(+601) 7293 6048</li>
      <li><b>Singapore</b>(+65) 9182 4637</li>
    </ul>
  </section>

  <section class="card card--front" aria-label="Card front">
    <span class="accent-tab"></span>
    <div class="person">
      <h1 class="person__name">Thomas Pirelli</h1>
      <p class="person__role">Director/Licensee-In-Charge</p>
    </div>

    <p class="wordmark">Brightmere Holdings</p>

    <ul class="contacts">
      <li>
        <svg viewBox="0 0 16 16" aria-hidden="true"><rect x="4" y="1.5" width="8" height="13" rx="1.5"/><line x1="7" y1="12" x2="9" y2="12"/></svg>
        0412 579 304
      </li>
      <li>
        <svg viewBox="0 0 16 16" aria-hidden="true"><path d="M3 2.5l2.5-.5 1.5 3-1.5 1.2a8 8 0 0 0 4.3 4.3L11 9l3 1.5-.5 2.5c-6 .5-11-4.5-10.5-10.5z"/></svg>
        (02) 7314 2296
      </li>
      <li>
        <svg viewBox="0 0 16 16" aria-hidden="true"><rect x="1.5" y="3.5" width="13" height="9" rx="1"/><path d="M1.5 4l6.5 5 6.5-5"/></svg>
        thomas@brightmere.com.au
      </li>
      <li>
        <svg viewBox="0 0 16 16" aria-hidden="true"><circle cx="8" cy="8" r="6.5"/><ellipse cx="8" cy="8" rx="2.8" ry="6.5"/><line x1="1.5" y1="8" x2="14.5" y2="8"/></svg>
        www.brightmereholdings.com
      </li>
      <li>
        <svg viewBox="0 0 16 16" aria-hidden="true"><path d="M8 14.5s-4.5-4.6-4.5-8a4.5 4.5 0 0 1 9 0c0 3.4-4.5 8-4.5 8z"/><circle cx="8" cy="6.5" r="1.6"/></svg>
        Level 9, 27 Harbour Lane W, Parramatta NSW 2150
      </li>
    </ul>
  </section>

</main>
</body>
</html>
```